Lorvika.no is a new website about pedagogical entrepreneurship. It's main target group is teachers. The Fjellmark Institute for Classroom Media and the Nordvik Agency for Schools and Study are leading the project.

The web page is meant to show examples of how different methods of entrepreneurship can be used pedagogical in a learning environment. The page will also support the user with examples of different teaching programs and other examples of best practice.

Pedagogical entrepreneurship is not about business and men in suits. It's a method for learning. The focus in the design should be on school, education and new ways of learning.

The final product should be motivating and engaging, but at the same time governmental and serious. We are not looking for something "flashy" and corporate-looking, but a moderate, task-focused and clean design that state quality.

We need designs for three pages:
1 - frontpage
2 - subpage ("Metoder og undervisningsopplegg")
3 - subpage ("Smått-VERK i Brekkelia")

The interaction design for these three pages will be uploaded as an attachment.

We would like you to find inspiration in the following websites:
- www.gryvekst.no
- www.lavrek.no
- www.tovandstudio.com
- www.kvp.no
(more will be added)

Please use the attached logo, and feel free to use this as an inspiration for the rest of the design.

Target Market(s)

Teachers

Industry/Entity Type

Education

Requirements
Must have
• * Header with: Logo. Main navigation. Utility navigation. Search box.
* Footer
Should not have
• Images of men in suits.
Very strong graphical elements that stands out too much (we want it clean).

```html
<!DOCTYPE html>
<html lang="en">
<head>
<meta charset="utf-8">
<title>Lorvika.no – Methods</title>
<link rel="stylesheet" href="https://fonts.googleapis.com/css2?family=Source+Sans+3:ital,wght@0,400;0,600;0,700;1,700&display=swap">
<style>
  :root{
    --navy:#02305f;
    --band:#6897c9;
    --panel:#cacaca;
    --row:#6897c9;
    --accent:#3399cc;
    --muted:#7f8fa6;
    --link:#555b66;
    --white:#ffffff;
    --font:"Source Sans 3", "Myriad Pro", Arial, sans-serif;
  }
  *{box-sizing:border-box;margin:0;padding:0}
  html,body{width:1200px;height:1101px;overflow:hidden}
  body{position:relative;background:var(--navy);font-family:var(--font);color:var(--navy)}
  a{color:inherit;text-decoration:none}

  /* header */
  .site-header{position:absolute;left:0;top:0;width:1200px;height:168px;background:var(--navy)}
  .brand{position:absolute;left:90px;top:42px;display:flex;align-items:center;gap:18px}
  .brand-mark{width:52px;height:52px;background:var(--white)}
  .brand-name{font-size:48px;font-weight:700;color:var(--accent);letter-spacing:-1px;line-height:1}
  .header-claim{position:absolute;right:98px;top:30px;text-align:right;color:var(--white)}
  .header-claim strong{display:block;font-size:22px;font-weight:700;font-style:italic;color:#b6d3f2;line-height:28px}
  .header-claim p{font-size:17.5px;line-height:22.5px;color:#d8e6f6}

  /* main nav band */
  .nav-band{position:absolute;left:0;top:168px;width:1200px;height:54px;background:var(--band)}
  .main-nav a{position:absolute;font-size:14.5px;font-weight:600;line-height:17px;text-transform:uppercase;color:var(--navy)}
  .main-nav .nav-what{left:168px;top:176px}
  .main-nav .nav-methods{left:338px;top:150px;width:174px;height:72px;background:var(--panel);padding:26px 0 0 31px}
  .main-nav .nav-examples{left:525px;top:176px}
  .search{position:absolute;left:861px;top:184px;display:flex;gap:7px}
  .search input{width:210px;height:23px;border:1px solid #9ab;background:var(--white);font:13px var(--font);padding:0 7px;color:#666}
  .search button{width:24px;height:24px;border:1px solid #8aa;background:#d9dde3;display:flex;align-items:center;justify-content:center}

  /* footer band */
  .footer-band{position:absolute;left:0;top:915px;width:1200px;height:186px;background:var(--band)}

  /* content panel */
  .panel{position:absolute;left:75px;top:222px;width:1058px;height:732px;background:var(--panel);box-shadow:10px 10px 16px rgba(0,0,0,.45)}

  .side-nav{position:absolute;left:0;top:28px;width:261px}
  .side-nav a{display:block;height:38px;padding-top:2px;border-bottom:1px solid var(--band);text-align:right;padding-right:4px;font-size:11px;font-weight:700;text-transform:uppercase;color:var(--navy);line-height:14px}
  .side-nav a + a{height:38px;padding-top:17px}

  .utility-nav{position:absolute;right:20px;top:21px;display:flex;gap:27px}
  .utility-nav a{font-size:14px;color:var(--link);text-decoration:underline}

  .intro{position:absolute;left:287px;top:58px;width:190px}
  .intro h1{font-size:25px;font-weight:700;color:var(--accent);letter-spacing:.5px;margin-bottom:20px}
  .intro p{font-size:13.5px;line-height:18px;color:var(--muted)}

  .plans{position:absolute;left:287px;top:208px;width:748px}
  .plans-title{height:23px;background:var(--navy);color:var(--white);font-size:13px;font-weight:600;text-transform:uppercase;padding:3px 7px}
  .filters{position:relative;height:35px}
  .filters .label{position:absolute;left:7px;top:6px;font-size:14px;color:#555}
  .select{position:absolute;top:6px;height:23px;border:1px solid var(--band);background:#d6d6d6;font-size:14px;color:#555;padding:2px 7px}
  .select::after{content:"";position:absolute;right:0;top:0;width:22px;height:21px;background:var(--band)}
  .select::before{content:"";position:absolute;right:6px;top:7px;z-index:1;border-left:5px solid transparent;border-right:5px solid transparent;border-top:6px solid var(--white)}
  .select-level{left:235px;width:78px}
  .select-time{left:410px;width:77px}
  .select-subject{left:577px;width:171px}

  .plan-list{list-style:none}
  .plan-row{position:relative;height:29px;margin-top:10px;background:var(--row);color:var(--white);font-size:13.5px;line-height:29px}
  .plan-row span{position:absolute}
  .plan-row .title{left:7px}
  .plan-row .level{left:242px}
  .plan-row .time{left:415px}
  .plan-row .subject{right:4px}

  /* footer content */
  .footer-mark{position:absolute;left:119px;top:987px;width:62px;height:62px;border-radius:50%;background:#eef3f9}
  .footer-col{position:absolute;top:985px;font-size:10px;line-height:13px}
  .footer-col h2{font-size:10px;font-weight:700;color:var(--white)}
  .footer-col p{color:var(--navy);margin-bottom:12px}
  .footer-col-main{left:231px}
  .footer-col-side{left:777px}
</style>
</head>
<body>
  <header class="site-header">
    <div class="brand">
      <span class="brand-mark"></span>
      <span class="brand-name">Lorvika</span>
    </div>
    <div class="header-claim">
      <strong>Pedagogical entrepreneurship works.</strong>
      <p>Lorem ipsum dolor sit amet, consectetur adipisicing elit,<br>sed fo eiusmod tempor incididunt ut labore<br>et dolore magna aliqua.</p>
    </div>
  </header>

  <div class="nav-band"></div>
  <div class="footer-band"></div>

  <main class="panel">
    <nav class="side-nav">
      <a href="#">Story line</a>
      <a href="#">Elevbedrift /ungdomsbedrift</a>
      <a href="#">Problembasert laering</a>
      <a href="#">Real</a>
      <a href="#">Uteskole-pedagogikk</a>
      <a href="#">Partnerskap</a>
      <a href="#">Prosjektarbeid</a>
      <a href="#">Kreative ekskursjoner</a>
      <a href="#">Gründercamp</a>
    </nav>

    <nav class="utility-nav">
      <a href="#">best pratice school</a>
      <a href="#">Try lorvikameter</a>
      <a href="#">about lorvika.no</a>
    </nav>

    <section class="intro">
      <h1>METHODS</h1>
      <p>text about the methods and how they can be used. Also an intro to how teachers can find teaching resources</p>
    </section>

    <section class="plans">
      <div class="plans-title">Find teaching plans</div>
      <div class="filters">
        <span class="label">Title</span>
        <span class="select select-level">Level</span>
        <span class="select select-time">Time</span>
        <span class="select select-subject">Subject</span>
      </div>
      <ul class="plan-list">
        <li class="plan-row"><span class="title">Title</span><span class="level">5-7 level</span><span class="time">2 weeks</span><span class="subject">Norwegian, Maths, English</span></li>
        <li class="plan-row"><span class="title">Title</span><span class="level">5-7 level</span><span class="time">2 weeks</span><span class="subject">Norwegian, Maths, English</span></li>
        <li class="plan-row"><span class="title">Title</span><span class="level">5-7 level</span><span class="time">2 weeks</span><span class="subject">Norwegian, Maths, English</span></li>
        <li class="plan-row"><span class="title">Title</span><span class="level">5-7 level</span><span class="time">2 weeks</span><span class="subject">Norwegian, Maths, English</span></li>
        <li class="plan-row"><span class="title">Title</span><span class="level">5-7 level</span><span class="time">2 weeks</span><span class="subject">Norwegian, Maths, English</span></li>
        <li class="plan-row"><span class="title">Title</span><span class="level">5-7 level</span><span class="time">2 weeks</span><span class="subject">Norwegian, Maths, English</span></li>
        <li class="plan-row"><span class="title">Title</span><span class="level">5-7 level</span><span class="time">2 weeks</span><span class="subject">Norwegian, Maths, English</span></li>
        <li class="plan-row"><span class="title">Title</span><span class="level">5-7 level</span><span class="time">2 weeks</span><span class="subject">Norwegian, Maths, English</span></li>
        <li class="plan-row"><span class="title">Title</span><span class="level">5-7 level</span><span class="time">2 weeks</span><span class="subject">Norwegian, Maths, English</span></li>
        <li class="plan-row"><span class="title">Title</span><span class="level">5-7 level</span><span class="time">2 weeks</span><span class="subject">Norwegian, Maths, English</span></li>
      </ul>
    </section>
  </main>

  <nav class="main-nav">
    <a class="nav-what" href="#">What is pedagogical<br>entrepreneurship</a>
    <a class="nav-methods" href="#">Methods and<br>teaching plans</a>
    <a class="nav-examples" href="#">Good examples/<br>best pratice</a>
  </nav>

  <form class="search">
    <input type="text" value="search ...">
    <button type="button" aria-label="Search">
      <svg width="14" height="14" viewBox="0 0 14 14"><circle cx="6" cy="6" r="4.2" fill="none" stroke="#fff" stroke-width="1.6"/><line x1="9" y1="9" x2="13" y2="13" stroke="#fff" stroke-width="1.8"/></svg>
    </button>
  </form>

  <footer>
    <span class="footer-mark"></span>
    <div class="footer-col footer-col-main">
      <h2>Pedagogical entrepreneurship</h2>
      <p>What is pedagogical entrepreneurship? | Science | Best pratice schools | Lorvikameteret | About lorvika.no</p>
      <h2>Gode eksempler</h2>
      <p>Smått-VERK at Brekkelia school | Smått-VERK at Brekkelia school | Smått-VERK at Brekkelia school | more...</p>
    </div>
    <div class="footer-col footer-col-side">
      <h2>Teaching Plans</h2>
      <p>Lorem ipsum | Lorem ipsum | Lorem ipsum | Lorem ipsum | more...</p>
      <h2>Methods</h2>
      <p>Story line | REAL | Café-pedagogikk | more...</p>
    </div>
  </footer>
</body>
</html>
```